Email Banner for Technology Company

We need a new email banner. The purpose of the email banner is to make us look more professional as a business and keep all communications with clients uniform. The previous designs which we have included below have now become outdated as our brand has developed and we need the new banner to become more aligned and modern.
We are a marketing organization that specialises in lead generation, email newsletters are sent to prospects on a regular basis. Therefore, it is important that we have an aesthetically pleasing banner as this is the first real impression prospects have our business. First impressions matter.
We are looking for a new email banner design as the current design is now outdated and does not reflect who we are as a business.
The new banners are required for launch at the start of Q2.
There is future work in the pipeline for the winning design. We have multiple industry sites that will require the new design as well as creating each of these in multiple languages.
The design must include the Brightwave Briefings wording the tagline 'The Technology Pro’s Research Hub'.
It needs to be creative and fun but still remain professional, sticking with the colour theme that already exists.

```html
<!DOCTYPE html>
<html lang="en">
<head>
<meta charset="utf-8">
<title>Brightwave Briefings – Email Banner Concepts</title>
<link rel="stylesheet" href="https://fonts.googleapis.com/css2?family=Montserrat:wght@400;700;800&display=swap">
<style>
  :root {
    --sheet: #2b2b2b;
    --navy: #00203f;
    --deep: #04395c;
    --teal: #0a4d74;
    --brand: #0096d6;
    --brand-mid: #0680c0;
    --white: #ffffff;
    --pale: #e6e6e6;
    --ink: #062a45;
  }
  * { box-sizing: border-box; margin: 0; padding: 0; }
  html, body { width: 1200px; height: 780px; overflow: hidden; background: var(--sheet); }
  body { position: relative; font-family: "Montserrat", Arial, sans-serif; }

  .banner {
    position: absolute; left: 66px; width: 1068px; height: 178px; overflow: hidden;
  }
  .banner--frame-dark { top: 61px; }
  .banner--diagonal { top: 300px; }
  .banner--frame-light { top: 541px; }

  .banner__glow {
    position: absolute; inset: 0;
    background:
      radial-gradient(ellipse 48% 38% at 66% 48%, #0aa3e6 0%, #0788c6 45%, rgba(4,70,110,0) 100%),
      linear-gradient(180deg, #04395c 0%, #0576b2 30%, #0576b2 70%, #04395c 100%);
  }
  .banner__shapes { position: absolute; inset: 0; }

  .cta {
    position: absolute; top: 0; right: 0; width: 126px; height: 28px;
    background: var(--white);
    clip-path: polygon(0 0, 100% 0, 100% 100%, 7px 100%, 0 78%);
    color: var(--ink); font-weight: 700; font-size: 14.5px; letter-spacing: .6px;
    display: flex; align-items: center; justify-content: center; padding-left: 6px;
  }
  .banner--diagonal .cta { clip-path: none; border-bottom-left-radius: 12px; }

  .brand {
    position: absolute; display: flex; align-items: center; gap: 7px;
    font-weight: 700; white-space: nowrap; letter-spacing: -.3px;
  }
  .brand__mark { display: block; background: var(--brand); flex: none; }
  .banner--frame-dark .brand { left: 56px; top: 76px; font-size: 19px; color: var(--white); }
  .banner--frame-dark .brand__mark { width: 19px; height: 19px; background: var(--white); }
  .banner--diagonal .brand { left: 52px; top: 72px; font-size: 28px; color: var(--white); }
  .banner--diagonal .brand__mark { width: 30px; height: 30px; background: var(--white); }
  .banner--frame-light .brand { left: 40px; top: 75px; font-size: 21px; color: var(--ink); }
  .banner--frame-light .brand__mark { width: 23px; height: 23px; }

  .tagline {
    position: absolute; color: var(--white); font-weight: 400; white-space: nowrap;
    text-shadow: 0 1px 3px rgba(0,20,40,.45);
  }
  .tagline strong { font-weight: 800; }
  .banner--frame-dark .tagline { left: 472px; top: 67px; font-size: 26.5px; }
  .banner--frame-light .tagline { left: 450px; top: 70px; font-size: 26.5px; }
  .banner--diagonal .tagline { left: 630px; top: 74px; font-size: 26px; line-height: 29px; text-shadow: none; }
  .banner--diagonal .tagline strong { display: block; }
</style>
</head>
<body>

<section class="banner banner--frame-dark">
  <div class="banner__glow" role="img" aria-label="Deep blue backdrop with a soft circuit-grid texture"></div>
  <svg class="banner__shapes" viewBox="0 0 1068 178" aria-hidden="true">
    <polygon points="1016,0 1068,0 1068,178 1052,178 1016,150" fill="#04507e" opacity=".8"/>
    <polygon points="0,20 330,20 366,52 366,157 0,157" fill="var(--navy)"/>
    <polygon points="0,30 326,30 356,57 356,147 0,147" fill="var(--teal)"/>
    <polygon points="0,40 322,40 346,61 346,137 0,137" fill="var(--white)"/>
    <polygon points="0,50 318,50 336,65 336,127 0,127" fill="var(--teal)"/>
    <polygon points="0,60 315,60 326,70 326,116 0,116" fill="var(--brand)"/>
  </svg>
  <div class="brand"><span class="brand__mark"></span>Brightwave Briefings</div>
  <p class="tagline">The Technology Pro’s <strong>Research Hub</strong></p>
  <div class="cta">CLICK HERE</div>
</section>

<section class="banner banner--diagonal">
  <svg class="banner__shapes" viewBox="0 0 1068 178" aria-hidden="true">
    <rect width="1068" height="178" fill="var(--brand-mid)"/>
    <polygon points="470,0 1068,0 1068,178 570,178" fill="var(--deep)" role="img" aria-label="Dark navy field with a faint scale pattern"/>
    <polygon points="395,0 414,0 448,60 437,63 429,58" fill="var(--pale)"/>
    <polygon points="410,0 431,0 482,88 466,88 460,80" fill="var(--brand)"/>
    <polygon points="431,0 446,0 528,135 522,138 510,133" fill="var(--navy)"/>
    <polygon points="453,0 457,0 552,162 548,164" fill="var(--white)"/>
    <polygon points="475,94 480,94 547,178 541,178" fill="var(--white)"/>
    <polygon points="474,100 478,100 531,178 525,178" fill="var(--brand)"/>
    <line x1="529" y1="142" x2="547" y2="174" stroke="var(--brand)" stroke-width="9" stroke-linecap="round"/>
    <line x1="552" y1="160" x2="560" y2="175" stroke="var(--navy)" stroke-width="9" stroke-linecap="round"/>
    <polygon points="1066,72 1068,72 1068,78 1004,178 1000,178" fill="var(--white)"/>
    <polygon points="1068,86 1068,116 1030,178 1012,178" fill="var(--navy)"/>
    <polygon points="1068,116 1068,150 1056,158 1048,150" fill="var(--brand)"/>
    <polygon points="1044,164 1048,164 1040,178 1036,178" fill="var(--brand)"/>
  </svg>
  <div class="brand"><span class="brand__mark"></span>Brightwave Briefings</div>
  <p class="tagline">The Technology Pro’s <strong>Research Hub</strong></p>
  <div class="cta">CLICK HERE</div>
</section>

<section class="banner banner--frame-light">
  <div class="banner__glow" role="img" aria-label="Deep blue backdrop with a soft circuit-grid texture"></div>
  <svg class="banner__shapes" viewBox="0 0 1068 178" aria-hidden="true">
    <polygon points="0,40 322,40 346,61 346,137 0,137" fill="var(--white)"/>
    <polygon points="0,50 318,50 336,65 336,127 0,127" fill="var(--teal)"/>
    <polygon points="0,60 315,60 326,70 326,117 0,117" fill="var(--white)"/>
  </svg>
  <div class="brand"><span class="brand__mark"></span>Brightwave Briefings</div>
  <p class="tagline">The Technology Pro’s <strong>Research Hub</strong></p>
  <div class="cta">CLICK HERE</div>
</section>

</body>
</html>
```